Relocation/furniture installation company needs new business cards

we are a relocation and furniture installation company mainly dealing with corporate clients and we are looking for new business card ideas. Cards should incorporate our logo and list our website, phone number and services. The company is only 2 years old but with more staff joining we are in the need for more business cards, so something with an awesome design that is eye catching would go a long way to insure we get our name out there and look good to potential new clients.

Target Market(s)

Corporate

Industry/Entity Type

Trade

Contact Information for Business Card

www.mervoline.co.nz
0508 4 bravok

furniture installation
business relocations
joinery installation
commercial property maintenance

Colors
0592cd
34a7d8
85cae6
85acd3
0356a4
cfdfed
cee9f5
757575
474747

Requirements
Must have
• Business relocations and furniture installation specialists
Nice to have
• something that incorporates our logo.

```html
<!DOCTYPE html>
<html lang="en">
<head>
<meta charset="utf-8">
<title>Mervoline Business Card</title>
<link href="https://fonts.googleapis.com/css2?family=Open+Sans:wght@400;600&display=swap" rel="stylesheet">
<style>
  :root {
    --backdrop: #e4e4e6;
    --card-paper: #f2f1ef;
    --brand-navy: #2b3a92;
    --edge-blue: #34a7d8;
    --panel-text: #e9eaf3;
    --bullet: #d6d8e6;
  }
  html, body {
    margin: 0;
    width: 1200px;
    height: 900px;
    overflow: hidden;
    background: var(--backdrop);
    font-family: "Open Sans", sans-serif;
  }
  .business-card {
    position: absolute;
    left: 111px;
    top: 148px;
    width: 978px;
    height: 605px;
    background: var(--card-paper);
    overflow: hidden;
    box-shadow: 0 6px 24px rgba(0,0,0,0.18);
  }
  .skyline-panel {
    position: absolute;
    inset: 0;
    width: 100%;
    height: 100%;
  }
  .contact-list, .service-list {
    position: absolute;
    margin: 0;
    padding: 0;
    list-style: none;
    color: var(--panel-text);
  }
  .contact-list {
    left: 58px;
    top: 194px;
    font-size: 28px;
    line-height: 41px;
  }
  .contact-list li {
    display: flex;
    align-items: center;
    gap: 8px;
  }
  .contact-icon {
    width: 24px;
    height: 24px;
    fill: var(--panel-text);
  }
  .service-list {
    left: 66px;
    top: 381px;
    font-size: 25px;
    line-height: 48px;
  }
  .service-list li {
    display: flex;
    align-items: center;
  }
  .service-list li::before {
    content: "";
    width: 14px;
    height: 14px;
    border-radius: 50%;
    background: var(--bullet);
    margin-right: 10px;
  }
  .brand-name {
    position: absolute;
    left: 686px;
    top: 238px;
    transform: translateX(-50%);
    margin: 0;
    font-size: 58px;
    font-weight: 600;
    line-height: 1;
    letter-spacing: 4px;
    color: var(--brand-navy);
    white-space: nowrap;
  }
</style>
</head>
<body>
  <main class="business-card">
    <svg class="skyline-panel" viewBox="0 0 652 403" preserveAspectRatio="none" aria-hidden="true">
      <polygon points="0,82 152,0 268,65 268,205 378,250 378,365 390,378 562,403 0,403" fill="var(--brand-navy)"/>
      <polyline points="152,0 268,65 268,205 378,250 378,365 390,378 562,403" fill="none" stroke="var(--edge-blue)" stroke-width="2.5"/>
    </svg>

    <ul class="contact-list">
      <li>
        <svg class="contact-icon" viewBox="0 0 24 24" aria-hidden="true"><path d="M6.6 10.8a15.1 15.1 0 0 0 6.6 6.6l2.2-2.2a1 1 0 0 1 1-.25 11.4 11.4 0 0 0 3.6.57 1 1 0 0 1 1 1V20a1 1 0 0 1-1 1A17 17 0 0 1 3 4a1 1 0 0 1 1-1h3.5a1 1 0 0 1 1 1c0 1.25.2 2.45.57 3.57a1 1 0 0 1-.25 1z"/></svg>
        0508 4 bravok
      </li>
      <li>
        <svg class="contact-icon" viewBox="0 0 24 24" aria-hidden="true"><path d="M12 2a10 10 0 1 0 0 20 10 10 0 0 0 0-20zm-1 17.9A8 8 0 0 1 4.2 10.2L9 15v1a2 2 0 0 0 2 2zm6.9-2.5A2 2 0 0 0 16 16h-1v-3a1 1 0 0 0-1-1H8v-2h2a1 1 0 0 0 1-1V7h2a2 2 0 0 0 2-2v-.4a8 8 0 0 1 2.9 12.8z"/></svg>
        www.mervoline.co.nz
      </li>
    </ul>

    <ul class="service-list">
      <li>Furniture Installation</li>
      <li>Business Relocations</li>
      <li>Joinery Installation</li>
      <li>Commercial Property Maintenance</li>
    </ul>

    <h1 class="brand-name">MERVOLINE</h1>
  </main>
</body>
</html>
```